Red fern bicycle rental

would like to have a bicycle rental website that has the ability to have a calender and be able to sign a liability waiver and pay all on line, We rent fat tire vorn bicycles

```html
<!DOCTYPE html>
<html lang="en">
<head>
<meta charset="utf-8">
<title>Red Fern Bicycle Rental</title>
<link rel="stylesheet" href="https://fonts.googleapis.com/css2?family=Arimo:wght@400;700&family=Lato:wght@400;700&display=swap">
<style>
:root{
  --blue:#1168b3;
  --blue-dark:#0b5aa0;
  --blue-light:#27a3df;
  --ink:#2b2b2b;
  --text:#444;
  --muted:#666;
  --quote:#c8c8c8;
  --footer:#2a2a2a;
  --white:#fff;
}
*{margin:0;padding:0;box-sizing:border-box}
html,body{width:1200px;height:4029px;overflow:hidden;background:var(--white)}
body{position:relative;font-family:Arimo,Arial,sans-serif;color:var(--ink)}
.abs{position:absolute}

/* header */
.brand{left:112px;top:30px;width:170px;display:flex;align-items:center;gap:8px;color:var(--blue);font-weight:700;font-size:19px;line-height:1.1}
.brand-dot{width:26px;height:26px;border-radius:50%;background:var(--blue);flex:none}
.phone{left:905px;top:14px;display:flex;align-items:center;gap:12px;color:var(--blue);font-size:17px;font-weight:700}
.phone-ico{width:34px;height:34px;border:2px solid var(--blue);border-radius:50%;display:flex;align-items:center;justify-content:center}
.nav{left:436px;top:76px;display:flex;font-size:18px;color:#333}
.nav a{color:inherit;text-decoration:none;margin-right:31px}
.nav a.active{color:var(--blue)}
.btn-login{left:984px;top:67px;width:97px;height:43px;background:var(--blue);color:#fff;font-size:18px;font-weight:700;display:flex;align-items:center;justify-content:center;border-radius:2px}

/* hero */
.hero-photo{left:0;top:133px;width:1200px;height:600px;background:linear-gradient(100deg,#cfd3d1 0%,#9ea7a6 35%,#5d5b52 60%,#8a8f8c 85%,#c9cdcb 100%)}
.hero-cut{left:0;top:620px}
.hero-title{left:105px;top:290px;font-size:40px;font-weight:700;color:var(--blue)}
.hero-sub{left:107px;top:350px;font-size:23px;font-weight:700;line-height:36px;color:#1e1e1e;width:540px}
.btn-hero{left:105px;top:445px;width:168px;height:45px;background:var(--blue);color:#fff;font-size:19px;display:flex;align-items:center;justify-content:center;border-radius:3px}
.dots{left:570px;top:662px;display:flex;gap:12px}
.dots i{width:10px;height:10px;border-radius:50%;background:#fff}
.dots i.on{background:var(--blue)}

/* section titles */
.sec-title{left:0;width:1200px;text-align:center;font-size:40px;font-weight:700;color:var(--ink)}

/* how it works */
.how-sub{left:0;top:855px;width:1200px;text-align:center;font-size:19px;color:#222}
.step{width:340px;text-align:center}
.step svg{display:block;margin:0 auto}
.step h3{margin-top:18px;font-size:19px;font-weight:400;color:var(--blue)}
.step p{margin-top:14px;font-size:14px;line-height:27px;color:var(--text)}

/* about */
.about-photo{left:0;top:1376px;width:560px;height:565px;background:linear-gradient(135deg,#3b2a1a 0%,#8a5a24 45%,#d39a3a 70%,#5a3a1c 100%);clip-path:polygon(0 0,505px 0,557px 535px,270px 565px,0 545px)}
.about-panel{left:0;top:1376px;width:1200px;height:531px;background:linear-gradient(180deg,var(--blue) 0%,var(--blue-light) 100%);clip-path:polygon(508px 0,1200px 0,1200px 531px,560px 531px)}
.about-title{left:578px;top:1445px;font-size:40px;font-weight:700;color:#fff}
.about-text{left:578px;top:1515px;width:495px;font-size:15.5px;line-height:32.5px;color:#fff;text-align:justify}
.btn-white{background:#fff;color:#222;font-size:15px;font-weight:700;display:flex;align-items:center;justify-content:center;border-radius:2px}

/* explore */
.card{top:2117px;width:254px;height:301px;border:2px solid #d6d6d6;background:#fff;box-shadow:0 2px 4px rgba(0,0,0,.08)}
.card .bike-photo{position:absolute;left:38px;top:75px;width:178px;height:120px;background:linear-gradient(180deg,#f1f3f4,#d9dee0);border-radius:4px}
.price{position:absolute;right:14px;top:18px;width:62px;height:62px;border-radius:50%;background:var(--blue);color:#fff;text-align:center;padding-top:10px}
.price b{display:block;font-size:25px;line-height:24px}
.price small{font-size:10px}
.card h4{position:absolute;left:0;top:215px;width:100%;text-align:center;font-size:17px;font-weight:700;color:#333}
.card .btn-view{position:absolute;left:45px;top:266px;width:162px;height:51px;border:2px solid #cfcfcf;background:#fff;color:var(--blue);font-size:19px;display:flex;align-items:center;justify-content:center;border-radius:3px}
.card .btn-view.on{background:var(--blue);border-color:var(--blue);color:#fff}
.arrow{top:2249px;width:36px;height:36px;border-radius:50%;border:1px solid #bbb;display:flex;align-items:center;justify-content:center;background:#fff}

/* booking */
.booking{left:0;top:2547px;width:1200px;height:353px;background:linear-gradient(180deg,var(--blue) 0%,var(--blue-light) 100%)}
.book-title{left:115px;top:2610px;font-size:40px;font-weight:700;color:#fff}
.book-text{left:117px;top:2685px;width:610px;font-size:16px;line-height:32px;color:#fff}
.calendar-art{left:765px;top:2552px;width:300px;height:311px;border-radius:12px;background:linear-gradient(180deg,#2a5fb8 0%,#2a5fb8 22%,#f2f2f2 22%,#e2e2e2 100%)}

/* testimonials */
.avatar{left:563px;top:3085px;width:120px;height:120px;border-radius:50%;border:3px solid var(--blue);background:linear-gradient(180deg,#e9eef2,#b8c3cc)}
.quote{font-family:Arimo,Arial,sans-serif;font-size:260px;font-weight:700;color:var(--quote);line-height:1}
.testi-text{left:215px;top:3226px;width:770px;text-align:center;font-family:Lato,sans-serif;font-size:14.5px;line-height:29px;color:#555}
.testi-name{left:0;top:3348px;width:1200px;text-align:center;font-family:Lato,sans-serif;font-size:16px;color:#333}
.tdots{left:570px;top:3389px;display:flex;gap:12px}
.tdots i{width:11px;height:11px;border-radius:50%;background:#222}
.tdots i.on{background:var(--blue)}

/* footer */
.footer-shape{left:0;top:3495px}
.f-brand{left:140px;top:3665px;color:#fff;font-weight:700;font-size:22px;display:flex;align-items:center;gap:10px}
.f-brand .brand-dot{background:#fff}
.f-text{left:131px;top:3746px;width:275px;font-size:14.5px;line-height:30.5px;color:#fff}
.social{top:3865px;width:40px;height:40px;border:2px solid #bbb;border-radius:50%}
.f-head{font-size:19px;font-weight:700;color:#fff}
.f-links{left:491px;top:3693px;font-family:Lato,sans-serif;font-size:17px;line-height:33.5px;color:#eee;list-style:none}
.f-sub{left:731px;top:3696px;width:330px;font-family:Lato,sans-serif;font-size:16px;line-height:27px;color:#eee}
.f-input{left:735px;top:3767px;width:275px;height:56px;background:#fff;font-family:Lato,sans-serif;font-size:16px;color:#555;padding:18px 16px}
.f-send{left:1017px;top:3767px;width:68px;height:56px;background:var(--blue);display:flex;align-items:center;justify-content:center}
.f-rule{left:110px;top:3946px;width:980px;height:1px;background:#777}
.f-copy{left:0;top:3978px;width:1200px;text-align:center;font-family:Lato,sans-serif;font-size:15px;color:#eee}
</style>
</head>
<body>

<header>
  <div class="abs brand"><span class="brand-dot"></span><span>RED FERN<br>BICYCLE RENTAL</span></div>
  <div class="abs phone">
    <span class="phone-ico"><svg width="18" height="18" viewBox="0 0 24 24"><path fill="#1168b3" d="M6.6 10.8a15 15 0 0 0 6.6 6.6l2.2-2.2a1 1 0 0 1 1-.25 11.4 11.4 0 0 0 3.6.57 1 1 0 0 1 1 1V20a1 1 0 0 1-1 1A17 17 0 0 1 3 4a1 1 0 0 1 1-1h3.5a1 1 0 0 1 1 1c0 1.250.2 2.450.57 3.6a1 1 0 0 1-.25 1z"/></svg></span>
    555-010-2468
  </div>
  <nav class="abs nav"><a class="active">Home</a><a>About</a><a>How It Works</a><a>Contact us</a><a>Sign Up</a></nav>
  <div class="abs btn-login">LOG IN</div>
</header>

<section class="hero">
  <div class="abs hero-photo" role="img" aria-label="Cyclist in a helmet racing a road bike along a coastal mountain road"></div>
  <svg class="abs hero-cut" width="1200" height="120" viewBox="0 0 1200 120">
    <polygon points="0,35 910,105 1200,18 1200,120 0,120" fill="#fff"/>
    <polyline points="0,36 910,106 1200,19" fill="none" stroke="#1168b3" stroke-width="5"/>
  </svg>
  <h1 class="abs hero-title">RED FERN BICYCLE RENTAL</h1>
  <p class="abs hero-sub">Neque porro quisquam est qui dolorem ipsum quia dolor sit amet, consectetur.</p>
  <div class="abs btn-hero">GET STARTED</div>
  <div class="abs dots"><i class="on"></i><i></i><i class="on"></i></div>
</section>

<section class="how">
  <h2 class="abs sec-title" style="top:772px">HOW IT WORKS</h2>
  <p class="abs how-sub">The leading booking platform for bike rentals</p>

  <div class="abs step" style="left:74px;top:935px">
    <svg width="200" height="200" viewBox="0 0 200 200">
      <rect x="31" y="31" width="138" height="138" rx="14" transform="rotate(45 100 100)" fill="none" stroke="#1168b3" stroke-width="6"/>
      <line x1="114" y1="8" x2="146" y2="40" stroke="#fff" stroke-width="10"/>
      <path d="M100 68a14 14 0 0 1 14 14c0 12-14 26-14 26s-14-14-14-26a14 14 0 0 1 14-14z" fill="none" stroke="#1168b3" stroke-width="3"/>
      <circle cx="100" cy="82" r="5" fill="none" stroke="#1168b3" stroke-width="3"/>
      <path d="M78 118h44l6 10H72z" fill="none" stroke="#1168b3" stroke-width="3"/>
    </svg>
    <h3>Find the perfect bike(s) for you</h3>
    <p>Sed ut perspiciatis unde omnis iste natus<br>error sit voluptatem accusantium doloremque<br>laudantium, totam rem aperiam,</p>
  </div>

  <div class="abs step" style="left:431px;top:935px">
    <svg width="200" height="200" viewBox="0 0 200 200">
      <rect x="31" y="31" width="138" height="138" rx="14" transform="rotate(45 100 100)" fill="none" stroke="#1168b3" stroke-width="6"/>
      <line x1="114" y1="8" x2="146" y2="40" stroke="#fff" stroke-width="10"/>
      <rect x="82" y="72" width="36" height="48" fill="none" stroke="#1168b3" stroke-width="3"/>
      <path d="M88 84h22M88 93h22M88 102h14" stroke="#1168b3" stroke-width="2.5"/>
      <path d="M124 82l-22 30-4 8 8-4 22-30z" fill="#fff" stroke="#1168b3" stroke-width="2.5"/>
    </svg>
    <h3>Book directly online</h3>
    <p>Sed ut perspiciatis unde omnis iste natus<br>error sit voluptatem accusantium doloremque<br>laudantium, totam rem aperiam,</p>
  </div>

  <div class="abs step" style="left:788px;top:935px">
    <svg width="200" height="200" viewBox="0 0 200 200">
      <rect x="31" y="31" width="138" height="138" rx="14" transform="rotate(45 100 100)" fill="none" stroke="#1168b3" stroke-width="6"/>
      <line x1="114" y1="8" x2="146" y2="40" stroke="#fff" stroke-width="10"/>
      <circle cx="76" cy="107" r="15" fill="none" stroke="#1168b3" stroke-width="3"/>
      <circle cx="124" cy="107" r="15" fill="none" stroke="#1168b3" stroke-width="3"/>
      <path d="M76 107l12-22h26l10 22M88 85l12 22 14-22M84 80h10M110 78h8" fill="none" stroke="#1168b3" stroke-width="3"/>
    </svg>
    <h3>The bike will be waiting for you!</h3>
    <p>Sed ut perspiciatis unde omnis iste natus<br>error sit voluptatem accusantium doloremque<br>laudantium, totam rem aperiam,</p>
  </div>
</section>

<section class="about">
  <div class="abs about-panel"></div>
  <div class="abs about-photo" role="img" aria-label="Close-up of a rider's shoe on the pedal of a mountain bike at sunset"></div>
  <h2 class="abs about-title">ABOUT US</h2>
  <p class="abs about-text">Sed ut perspiciatis unde omnis iste natus error sit voluptatem accusantium doloremque laudantium, totam rem aperiam, eaque ipsa quae ab illo inventore veritatis et quasi architecto beatae vitae dicta sunt explicabo. Nemo enim ipsam voluptatem quia voluptas sit aspernatur aut odit aut fugit, sed quia consequuntur magni dolores eos qui ratione voluptatem sequi nesciunt. Neque porro quisquam est, qui dolorem ipsum quia dolor sit amet, consectetur, adipisci velit, sed quia non numquam eius modi tempora incidunt ut labore et dolore.</p>
  <div class="abs btn-white" style="left:580px;top:1800px;width:130px;height:45px">READ MORE</div>
</section>

<section class="explore">
  <h2 class="abs sec-title" style="top:1998px">EXPLORE RED FERN BICYCLE</h2>
  <div class="abs arrow" style="left:103px"><svg width="12" height="12" viewBox="0 0 12 12"><path d="M8 1L3 6l5 5" fill="none" stroke="#555" stroke-width="1.6"/></svg></div>
  <div class="abs arrow" style="left:1061px"><svg width="12" height="12" viewBox="0 0 12 12"><path d="M4 1l5 5-5 5" fill="none" stroke="#555" stroke-width="1.6"/></svg></div>

  <div class="abs card" style="left:165px">
    <div class="bike-photo" role="img" aria-label="Teal and black fat tire rental bicycle"></div>
    <div class="price"><b>$15</b><small>Per day</small></div>
    <h4>RED FERN BICYCLE</h4>
    <div class="btn-view">VIEW DETAILS</div>
  </div>
  <div class="abs card" style="left:473px">
    <div class="bike-photo" role="img" aria-label="Dark grey fat tire rental bicycle"></div>
    <div class="price"><b>$17</b><small>Per day</small></div>
    <h4>RED FERN BICYCLE</h4>
    <div class="btn-view on">VIEW DETAILS</div>
  </div>
  <div class="abs card" style="left:781px">
    <div class="bike-photo" role="img" aria-label="Black fat tire rental bicycle"></div>
    <div class="price"><b>$15</b><small>Per day</small></div>
    <h4>RED FERN BICYCLE</h4>
    <div class="btn-view">VIEW DETAILS</div>
  </div>
</section>

<section>
  <div class="abs booking"></div>
  <h2 class="abs book-title">ONLINE RENTAL BOOKING</h2>
  <p class="abs book-text">Sed ut perspiciatis unde omnis iste natus error sit voluptatem accusantium doloremque laudantium, totam rem aperiam, eaque ipsa quae ab illo inventore veritatis et quasi architecto beatae vitae dicta sunt explicabo.</p>
  <div class="abs btn-white" style="left:116px;top:2800px;width:124px;height:45px">BOOK NOW</div>
  <div class="abs calendar-art" role="img" aria-label="Illustration of a monthly desk calendar with a blue header"></div>
</section>

<section class="testimonials">
  <h2 class="abs sec-title" style="top:2975px;left:9px">TESTIMONIALS</h2>
  <div class="abs avatar" role="img" aria-label="Portrait of a smiling cyclist customer"></div>
  <div class="abs quote" style="left:140px;top:3126px">&ldquo;</div>
  <div class="abs quote" style="left:993px;top:3239px">&rdquo;</div>
  <p class="abs testi-text">Sed ut perspiciatis unde omnis iste natus error sit voluptatem accusantium doloremque laudantium, totam rem aperiam, eaque ipsa quae ab illo inventore veritatis et quasi architecto beatae vitae dicta sunt explicabo. Nemo enim ipsam voluptatem quia voluptas.</p>
  <p class="abs testi-name">By Client Name</p>
  <div class="abs tdots"><i></i><i></i><i class="on"></i></div>
</section>

<footer>
  <svg class="abs footer-shape" width="1200" height="534" viewBox="0 0 1200 534">
    <polygon points="0,85 290,5 1200,68 1200,534 0,534" fill="#2a2a2a"/>
    <polyline points="0,84 290,4 1200,67" fill="none" stroke="#1168b3" stroke-width="6"/>
  </svg>
  <div class="abs f-brand"><span class="brand-dot"></span><span>RED FERN</span></div>
  <p class="abs f-text">Sed ut perspiciatis unde omnis iste natus error sit voluptatem accusantium doloremque laudantium, totam rem</p>
  <div class="abs social" style="left:125px" role="img" aria-label="Social profile link"></div>
  <div class="abs social" style="left:180px" role="img" aria-label="Social profile link"></div>
  <div class="abs social" style="left:235px" role="img" aria-label="Social profile link"></div>

  <h3 class="abs f-head" style="left:491px;top:3645px;font-size:18px">QUICK LINKS</h3>
  <ul class="abs f-links"><li>Home</li><li>About</li><li>How It Works</li><li>Contact us</li><li>Sign Up</li></ul>

  <h3 class="abs f-head" style="left:726px;top:3645px;font-size:20px">SUBSCRIBE TO NEWSLETTER</h3>
  <p class="abs f-sub">Lorem ipsum dolor sit amet, consectetur adipiscing elit,</p>
  <div class="abs f-input">Enter Your Email</div>
  <div class="abs f-send"><svg width="22" height="22" viewBox="0 0 24 24"><path fill="#fff" d="M22 2L2 10.5l6.5 2.5L19 5l-8.5 9.5V21l3.5-4.5 4.5 3.5z"/></svg></div>

  <div class="abs f-rule"></div>
  <p class="abs f-copy">© 2020 All Rights Reserved | Privacy Policy | Terms and Conditions</p>
</footer>

</body>
</html>
```